Business Card Design Project

Crestline Vein Center

Dr Tomas Venrick M.D, F.R.C.S
Vascular and Vein Surgery

47-18 Pellham Avenue, Suite 314
Millbrook
NY 11287

212-555-0147
718-555-0193
www.crestlinecare.us back of the card for scheduled appointments up to 5 appointment dates

Target Market(s)

Male and Female patients from 25 onwards with spider veins or varicose veins

Industry/Entity Type

Business

Font styles to use
Serif

Colors
86cae6
85abd2
0456a4

Requirements
Must have
• Modern Sophisticated design using light blue and grey text
Should not have
• hearts or flowers

```html
<!DOCTYPE html>
<html lang="en">
<head>
<meta charset="utf-8">
<title>Crestline Vein Center – Business Card</title>
<link rel="stylesheet" href="https://fonts.googleapis.com/css2?family=EB+Garamond:wght@400;600;700&display=swap">
<style>
  :root {
    --brand-blue: #0456a4;
    --mid-blue: #85abd2;
    --sky-blue: #86cae6;
    --ink: #333333;
    --slot-ink: #e8eef7;
    --white: #ffffff;
  }
  * { box-sizing: border-box; margin: 0; padding: 0; }
  html, body { width: 1050px; height: 1200px; overflow: hidden; background: var(--white); }
  body { font-family: "EB Garamond", Garamond, serif; position: relative; }

  .card-front {
    position: absolute; left: 0; top: 0; width: 1050px; height: 588px;
    background: radial-gradient(ellipse at 30% 45%, #ffffff 0%, #f4f4f4 55%, #e6e6e6 100%);
  }
  .brand { position: absolute; left: 100px; top: 112px; display: flex; align-items: center; gap: 22px; }
  .brand-dot { width: 60px; height: 60px; border-radius: 50%; background: var(--brand-blue); flex: none; }
  .brand-name { color: var(--brand-blue); font-weight: 600; font-size: 58px; line-height: 1; }

  .doctor-name { position: absolute; left: 97px; top: 296px; color: var(--brand-blue); font-weight: 700; font-size: 35px; }
  .specialty { position: absolute; left: 97px; top: 340px; color: var(--ink); font-size: 26px; }
  .divider { position: absolute; left: 97px; top: 384px; width: 525px; height: 2px; background: var(--brand-blue); }

  .contact-row { position: absolute; left: 97px; display: flex; align-items: center; gap: 18px; color: var(--ink); font-size: 28px; }
  .contact-row.phone { top: 410px; }
  .contact-row.web { top: 455px; }
  .contact-icon { width: 32px; height: 32px; border-radius: 5px; background: var(--brand-blue); display: flex; align-items: center; justify-content: center; }
  .address { position: absolute; left: 97px; top: 505px; color: var(--ink); font-size: 26px; line-height: 36px; }

  .band-split { position: absolute; left: 0; top: 588px; width: 1050px; height: 12px; display: flex; }
  .band-split .dark { width: 527px; background: var(--brand-blue); }
  .band-split .light { flex: 1; background: var(--mid-blue); }

  .card-back {
    position: absolute; left: 0; top: 602px; width: 1050px; height: 586px;
    background: var(--brand-blue); color: var(--white);
  }
  .band-foot { position: absolute; left: 0; top: 1188px; width: 1050px; height: 12px; background: var(--mid-blue); }

  .appointment-title {
    position: absolute; left: 0; width: 1050px; top: 88px; text-align: center;
    font-weight: 700; font-size: 36px; letter-spacing: 0.5px; text-decoration: underline; text-underline-offset: 5px; text-decoration-thickness: 2px;
  }
  .slot { position: absolute; font-size: 22px; line-height: 33.5px; color: var(--slot-ink); }
  .slot p { white-space: nowrap; display: flex; width: 316px; }
  .slot .label { width: 70px; flex: none; }
  .slot .leader { letter-spacing: 3.2px; overflow: hidden; }
  .slot.a { left: 60px; top: 175px; }
  .slot.b { left: 678px; top: 175px; }
  .slot.c { left: 60px; top: 314px; }
  .slot.d { left: 678px; top: 314px; }
  .slot.e { left: 369px; top: 462px; }
</style>
</head>
<body>
  <section class="card-front">
    <div class="brand">
      <span class="brand-dot"></span>
      <span class="brand-name">Crestline Vein<br>Center</span>
    </div>
    <h1 class="doctor-name">Dr Tomas Venrick M.D, F.R.C.S</h1>
    <p class="specialty">Vascular and Vein Surgery</p>
    <div class="divider"></div>

    <div class="contact-row phone">
      <span class="contact-icon">
        <svg width="16" height="24" viewBox="0 0 16 24" aria-hidden="true">
          <rect x="2" y="1" width="12" height="22" rx="2" fill="none" stroke="#fff" stroke-width="2"/>
          <rect x="5" y="4" width="6" height="6" fill="#fff"/>
          <circle cx="8" cy="18" r="1.5" fill="#fff"/>
        </svg>
      </span>
      <span>212-555-0147 | 718-555-0193</span>
    </div>
    <div class="contact-row web">
      <span class="contact-icon">
        <svg width="24" height="24" viewBox="0 0 24 24" aria-hidden="true" fill="none" stroke="#fff" stroke-width="1.6">
          <circle cx="12" cy="12" r="10"/>
          <ellipse cx="12" cy="12" rx="4.5" ry="10"/>
          <line x1="2" y1="12" x2="22" y2="12"/>
          <path d="M4 7h16M4 17h16"/>
        </svg>
      </span>
      <span>www.crestlinecare.us</span>
    </div>
    <p class="address">47-18 Pellham Avenue, Suite 314<br>Millbrook, NY 11287</p>
  </section>

  <div class="band-split"><span class="dark"></span><span class="light"></span></div>

  <section class="card-back">
    <h2 class="appointment-title">APPOINTMENT</h2>
    <div class="slot a"><p><span class="label">Date:</span><span class="leader">..............................</span></p><p><span class="label">Time:</span><span class="leader">..............................</span></p><p><span class="label">Name:</span><span class="leader">..............................</span></p></div>
    <div class="slot b"><p><span class="label">Date:</span><span class="leader">..............................</span></p><p><span class="label">Time:</span><span class="leader">..............................</span></p><p><span class="label">Name:</span><span class="leader">..............................</span></p></div>
    <div class="slot c"><p><span class="label">Date:</span><span class="leader">..............................</span></p><p><span class="label">Time:</span><span class="leader">..............................</span></p><p><span class="label">Name:</span><span class="leader">..............................</span></p></div>
    <div class="slot d"><p><span class="label">Date:</span><span class="leader">..............................</span></p><p><span class="label">Time:</span><span class="leader">..............................</span></p><p><span class="label">Name:</span><span class="leader">..............................</span></p></div>
    <div class="slot e"><p><span class="label">Date:</span><span class="leader">..............................</span></p><p><span class="label">Time:</span><span class="leader">..............................</span></p><p><span class="label">Name:</span><span class="leader">..............................</span></p></div>
  </section>
  <div class="band-foot"></div>
</body>
</html>
```